Heritage Hollow Business Cards

Require a business card design. <br/><br/>Needs to include logo (either round or long version) plus these details:<br/>Maya Torvel<br/>Heritage Hollow<br/>maya@quonbrook.com.au<br/>02 6481 7390<br/>PO Box Glenwarra NSW 2913<br/>www.heritagehollow.com.au<br/><br/>I need in an editable format so that I can create for multiple staff members. <br/><br/>

Target Market(s)

We are an online store selling renovation products to home owners are builders. Looking for a classic classy design.

Industry/Entity Type

Home And Garden

Contact Information for Business Card

Maya Torvel
Heritage Hollow
maya@quonbrook.com.au
02 6481 7390
PO Box Glenwarra NSW 2913
www.heritagehollow.com.au

Colors

Designer to choose colors to be used in the design.

Requirements
Must have
• Must include Logo.

```html
<!DOCTYPE html>
<html lang="en">
<head>
<meta charset="utf-8">
<title>Heritage Hollow Business Cards</title>
<link href="https://fonts.googleapis.com/css2?family=Libre+Baskerville:wght@400;700&family=Open+Sans:wght@400&display=swap" rel="stylesheet">
<style>
  :root {
    --backdrop: #1c1c1e;
    --card-black: #060606;
    --card-white: #ffffff;
    --band-dark: #231f20;
    --accent-green: #0e8a6c;
    --silver: #cfcfcf;
    --logo-grey: #3a3a3a;
    --contact-text: #e6e6e6;
    --icon-green: #5fa58f;
  }
  * { margin: 0; padding: 0; box-sizing: border-box; }
  html, body { width: 1200px; height: 960px; overflow: hidden; }
  body {
    background: var(--backdrop);
    display: flex;
    flex-direction: column;
    align-items: center;
    justify-content: center;
    gap: 40px;
  }
  .card {
    position: relative;
    width: 720px;
    height: 400px;
    overflow: hidden;
    box-shadow: 0 10px 30px rgba(0,0,0,0.45);
  }

  /* Back of card */
  .card-back {
    background: var(--card-black);
    display: flex;
    align-items: center;
    justify-content: center;
    gap: 22px;
  }
  .card-back .brand-mark {
    width: 54px; height: 54px;
    border: 2px solid var(--silver);
    border-radius: 50%;
  }
  .card-back .brand-name {
    font-family: "Libre Baskerville", serif;
    font-weight: 700;
    font-size: 54px;
    color: var(--silver);
    letter-spacing: 1px;
  }

  /* Front of card */
  .card-front { background: var(--card-white); }
  .card-front .band {
    position: absolute; inset: 0;
    width: 100%; height: 100%;
  }
  .card-front .brand {
    position: absolute;
    left: 40px; top: 44px;
    display: flex; align-items: center; gap: 14px;
  }
  .card-front .brand-mark {
    width: 40px; height: 40px;
    border: 2px solid var(--logo-grey);
    border-radius: 50%;
  }
  .card-front .brand-name {
    font-family: "Libre Baskerville", serif;
    font-weight: 700;
    font-size: 38px;
    color: var(--logo-grey);
  }
  .contact-list {
    position: absolute;
    left: 36px; top: 232px;
    list-style: none;
    font-family: "Open Sans", sans-serif;
    font-size: 17px;
    color: var(--contact-text);
    line-height: 28px;
  }
  .contact-list li { display: flex; align-items: center; gap: 8px; }
  .contact-list svg { width: 14px; height: 14px; flex: none; }
  .contact-list .address { margin-left: -8px; }
  .name-tab {
    position: absolute;
    left: 452px; top: 252px;
    width: 210px; height: 82px;
    background: var(--accent-green);
    border-radius: 26px;
    display: flex; flex-direction: column;
    align-items: center; justify-content: center;
    color: #ffffff;
    font-family: "Libre Baskerville", serif;
    font-weight: 700;
  }
  .name-tab .person { font-size: 24px; }
  .name-tab .role { font-size: 15px; margin-top: 2px; }
</style>
</head>
<body>
  <section class="card card-back">
    <span class="brand-mark"></span>
    <span class="brand-name">Heritage Hollow</span>
  </section>

  <section class="card card-front">
    <svg class="band" viewBox="0 0 720 400" preserveAspectRatio="none" aria-hidden="true">
      <path d="M0 205 L440 278 C470 283 470 300 500 304 L720 336 L720 400 L0 400 Z" fill="var(--band-dark)"/>
    </svg>

    <div class="brand">
      <span class="brand-mark"></span>
      <span class="brand-name">Heritage Hollow</span>
    </div>

    <ul class="contact-list">
      <li>
        <svg viewBox="0 0 24 24"><path fill="var(--icon-green)" d="M6.6 10.8a15 15 0 0 0 6.6 6.6l2.2-2.2c.3-.3.7-.4 1-.2 1.1.4 2.3.6 3.6.6.6 0 1 .4 1 1V20c0 .6-.4 1-1 1A17 17 0 0 1 3 4c0-.6.4-1 1-1h3.5c.6 0 1 .4 1 1 0 1.3.2 2.5.6 3.6.1.3 0 .7-.2 1z"/></svg>
        02 6481 7390
      </li>
      <li>
        <svg viewBox="0 0 24 24"><path fill="var(--icon-green)" d="M2 5h20v14H2zM3.5 6.5 12 13l8.5-6.5"/><path fill="none" stroke="var(--band-dark)" stroke-width="1.6" d="M2.5 5.5 12 13l9.5-7.5"/></svg>
        maya@quonbrook.com.au
      </li>
      <li>
        <svg viewBox="0 0 24 24"><g fill="none" stroke="var(--icon-green)" stroke-width="2"><circle cx="12" cy="12" r="9"/><path d="M3 12h18M12 3c3 3 3 15 0 18M12 3c-3 3-3 15 0 18"/></g></svg>
        www.heritagehollow.com.au
      </li>
      <li class="address">PO Box Glenwarra NSW 2913</li>
    </ul>

    <div class="name-tab">
      <span class="person">Maya Torvel</span>
      <span class="role">Director</span>
    </div>
  </section>
</body>
</html>
```